Harbinger Noble Alloys Works Business Cards

We are wanting to have a new business card designed for our company as we go to a convention. We want to balance business/Modern with elegance and beauty. Our company sells highend jewelry pieces. We want to utilize the colors of Black and Gold and have gold foiled fonts to be physically printed on the business cards.
We also would like to have space to write notes on the back side of the business card. When we meet people at jewelry conventions we would like to write notes if possible.
Here are websites and designs that we like the look and feel of these companies and you can use these as design ideas.
https://www.lorvanne.com
https://www.bellquist.com/en-us/home
Here is our company website link
www.harbingernaw.com
I also up loaded two versions of our logo.
- Update 4.26.22
I have uploaded photos of a business card we like. this card has raised embossed letters that you can feel. the raise letters are like a plastic but we don't need to use that...I uploaded to show you that we like the experience of the client feeling the characters of the logo. we also would like to have the material as a satin or some material very soft.
- Maybe we can get designs with beautiful gold foiling and raised characters and logos. we like simplicity...not busy but an elegant design. We need to write notes and would like a section where we can write notes. but we want an elegant style and the client has an experience with the feel of the card when they touch the card.
Colors
- Main colors Black & Gold
- white or light colors for small notes section.
Specialty ideals and things we would like to see based on your design styles.
- raised fonts
- raised logos
- gold foiling
- satin/soft finish on the card material.
we are wanting to design a business card that looks elegant and clean. When the client is handed the business card we want them to physically experience the business card as well by touching the raised logos or fonts and the base material is soft satin. I hope this helps with further designs.
thank you all
We uploaded a new contact layout that we have designed in our office. we would like to see how this would look on your designs.
thank you
I just finished uploading the Contact Layout. the colors are just examples. please use this layout as an idea and use colors based on the feed back we have given each of you personally.
Contact Information for Business Card
we need an area to write notes, we would like to have our logos or the diamond of our logo or the business card to have embossed sections to the business card so when the customer touches the card they can feel the logo. we would also like sections of our business card to have gold foiling. we would also like to use a satin soft paper with our card. when the client touches the card its super soft and high quality
Requirements
Must have
- we would like to have our logos or the diamond of our logo or the business card to have embossed sections to the business card so when the customer touches the card they can feel the logo. we would also like sections of our business card to have gold foiling. we would also like to use a satin soft paper with our card. when the client touches the card its super soft and high quality
Nice to have
- we would like to have our logos or the diamond of our logo or the business card to have embossed sections to the business card so when the customer touches the card they can feel the logo. we would also like sections of our business card to have gold foiling.

```html
<!DOCTYPE html>
<html lang="en">
<head>
<meta charset="utf-8">
<title>Harbinger Noble Alloys Works — Business Cards</title>
<link rel="stylesheet" href="https://fonts.googleapis.com/css2?family=Arvo:wght@700&family=Montserrat:wght@400;600&display=swap">
<style>
  :root {
    --stage: #1c1c1c;
    --card-black: #151515;
    --card-white: #ffffff;
    --gold: #b8891a;
    --gold-bright: #e3c24a;
    --gold-deep: #a47512;
    --note-fill: #ffffff;
  }
  * { box-sizing: border-box; margin: 0; padding: 0; }
  html, body { width: 1200px; height: 900px; overflow: hidden; }
  body {
    background: var(--stage);
    position: relative;
    font-family: "Montserrat", sans-serif;
  }
  .card {
    position: absolute;
    left: 290px;
    width: 620px;
    height: 354px;
    border-radius: 2px;
    box-shadow: 0 18px 40px rgba(0,0,0,.55);
  }

  /* Back side — black with notes area */
  .card-back {
    top: 60px;
    background: var(--card-black);
    padding-top: 58px;
  }
  .back-brand {
    display: flex;
    justify-content: center;
    align-items: center;
    gap: 12px;
    height: 40px;
  }
  .back-brand .mark {
    width: 20px; height: 20px;
    border-radius: 50%;
    background: var(--gold-bright);
  }
  .back-brand .wordmark {
    font-family: "Montserrat", sans-serif;
    font-weight: 600;
    font-size: 26px;
    color: var(--gold-bright);
  }
  .ornament-band {
    display: block;
    margin: 0 auto;
    width: 390px;
    height: 30px;
    border-radius: 15px;
    background: linear-gradient(90deg, rgba(227,194,74,0) 0%, rgba(227,194,74,.45) 30%, rgba(227,194,74,.6) 50%, rgba(227,194,74,.45) 70%, rgba(227,194,74,0) 100%);
  }
  .ornament-top { margin-top: 44px; }
  .ornament-bottom { margin-top: 8px; }
  .notes-area {
    width: 410px;
    height: 62px;
    margin: 8px auto 0;
    background: var(--note-fill);
    border-radius: 14px;
  }

  /* Front side — white with contact details */
  .card-front {
    top: 470px;
    background: var(--card-white);
    padding: 36px 50px 0 50px;
  }
  .logo-spot {
    display: flex;
    align-items: center;
    gap: 10px;
    margin-left: 30px;
    height: 86px;
  }
  .logo-spot .mark {
    width: 22px; height: 22px;
    border-radius: 50%;
    background: var(--gold-bright);
  }
  .logo-spot .wordmark {
    font-family: "Montserrat", sans-serif;
    font-weight: 600;
    font-size: 20px;
    color: var(--gold);
  }
  .person-name {
    margin-top: 30px;
    font-family: "Arvo", serif;
    font-weight: 700;
    font-size: 22px;
    letter-spacing: 1px;
    color: var(--gold-deep);
  }
  .person-role {
    font-size: 15px;
    color: var(--gold);
    margin-top: -2px;
  }
  .address {
    margin-top: 14px;
    font-size: 15px;
    color: var(--gold);
    padding-bottom: 8px;
    border-bottom: 1.5px solid var(--gold);
    width: 500px;
  }
  .contact-line {
    margin-top: 8px;
    font-size: 15px;
    color: var(--gold);
    line-height: 1.45;
  }
  .contact-line b { font-weight: 600; }
  .contact-line + .contact-line { margin-top: 0; }
</style>
</head>
<body>

  <section class="card card-back" aria-label="Card back">
    <div class="back-brand">
      <span class="mark"></span>
      <span class="wordmark">Harbinger Noble Alloys</span>
    </div>
    <div class="ornament-band ornament-top" role="img" aria-label="Gold filigree flourish divider"></div>
    <div class="notes-area" aria-label="Space for handwritten notes"></div>
    <div class="ornament-band ornament-bottom" role="img" aria-label="Gold filigree flourish divider"></div>
  </section>

  <section class="card card-front" aria-label="Card front">
    <div class="logo-spot">
      <span class="mark"></span>
      <span class="wordmark">Harbinger Noble Alloys</span>
    </div>
    <h2 class="person-name">JULIAN MARLOWE</h2>
    <p class="person-role">Director</p>
    <p class="address">2140 Lindenfield Rd NE Corvallis, Oregon USA 97330</p>
    <p class="contact-line"><b>Phone:</b> (503) 555-0147 | <b>Email:</b> info@harbingernaw.com</p>
    <p class="contact-line"><b>Web:</b> www.harbingernaw.com</p>
  </section>

</body>
</html>
```